Maple Jubilee 2017 Poster

We need a poster design for our private school's annual Maple Jubilee. We're a progressive school in nyc, with deep community roots and a rich hundred year history. The community cherishes the events and looks forward to seeing what excitement each new year will bring! The posters will be displayed thoughout the school, appealing to a diverse audience of children and their' families.
We'd like a vintage vibe, circa turn of the 20th century (1900s). Please reference the images I've included, which give some inspiration. Also, as pertains to the theme, I'd like a representation of a vintage apple basket, brimming with apples, but with a planet earth nestled inside as the main focal point. Kind of like a words fair meets the harvest...
Also typography should be semi old fashioned looking as well.
COPY - Should Include the following:

Brook & Meadow
Maple Jubilee of Peoples

October 14th 12:00-4:00pm
Celebrate an Afternoon of Great Food, Music, Entertainment, & Fun

Tickets will be available for sale at Pickup

Target Market(s)

School Community, children and their parents, faculty, etc.

Industry/Entity Type

School

Font styles to use
Other font styles liked:
• Something old world fair, country looking

Colors
ec1f27
fcca95
ffcf3e

Requirements
Must have
• We'd like a vintage vibe, circa turn of the 20th century (1900s). Please reference the images I've included, which give some inspiration. Also, as pertains to the theme, I'd like a representation of a vintage apple basket, brimming with apples, but with a planet earth nestled inside as the main focal point. Kind of like a words fair meets the harvest...
• Also typography should be semi old fashioned looking as well.
• COPY - Should Include the following:
• Brook & Meadow
• Maple Jubilee of Peoples
• October 14th 12:00-4:00pm
• Celebrate an Afternoon of Great Food, Music, Entertainment, & Fun
• Tickets will be available for sale at Pickup
Nice to have
• Attractive design, draws you in, gets you interested in the event, informs you of important details.
Should not have
• I think that the design ask is pretty straight forward.

```html
<!DOCTYPE html>
<html lang="en">
<head>
<meta charset="utf-8">
<title>Maple Jubilee of Peoples – Poster</title>
<link href="https://fonts.googleapis.com/css2?family=Anton&family=Lobster&family=Luckiest+Guy&family=Open+Sans:wght@600;700&family=Oswald:wght@500&display=swap" rel="stylesheet">
<style>
  :root {
    --red: #ec1f27;
    --peach: #fcca95;
    --gold: #ffcf3e;
    --sky-top: #f6b25a;
    --sky-mid: #fbd08f;
    --sky-low: #fde2b0;
    --cream: #fdf5dc;
    --brown: #8b4522;
    --shadow-brown: #7a3a1c;
    --ink: #111111;
    --frame: #7cc3c0;
    --white: #ffffff;
  }
  * { margin: 0; padding: 0; box-sizing: border-box; }
  html, body { width: 848px; height: 1200px; overflow: hidden; background: var(--peach); }
  .poster {
    position: relative;
    width: 848px; height: 1200px;
    overflow: hidden;
    background: radial-gradient(ellipse at 50% 45%, var(--sky-low) 0%, var(--sky-mid) 45%, var(--sky-top) 100%);
  }
  .layer { position: absolute; left: 0; top: 0; width: 848px; height: 1200px; pointer-events: none; }

  .banner-title {
    position: absolute; left: 0; top: 112px; width: 848px; height: 110px;
    text-align: center;
    font-family: "Anton", sans-serif;
    font-size: 92px; line-height: 110px;
    color: var(--gold);
    letter-spacing: 1px;
  }

  .event-title {
    position: absolute; left: 0; width: 848px; text-align: center;
    font-family: "Lobster", cursive;
    color: var(--red);
    line-height: 1;
    text-shadow:
      -3px -3px 0 var(--cream), 3px -3px 0 var(--cream), -3px 3px 0 var(--cream), 3px 3px 0 var(--cream),
      0 -4px 0 var(--cream), 0 4px 0 var(--cream), -4px 0 0 var(--cream), 4px 0 0 var(--cream),
      6px 7px 0 var(--shadow-brown), 8px 9px 0 var(--shadow-brown);
  }
  .event-title--line1 { top: 290px; font-size: 140px; }
  .event-title--line2 { top: 405px; font-size: 150px; }
  .event-title--line3 { top: 522px; font-size: 150px; }

  .event-date {
    position: absolute; left: 280px; top: 700px;
    font-family: "Open Sans", sans-serif; font-weight: 700;
    font-size: 39px; line-height: 1.2; color: var(--ink); letter-spacing: -0.3px;
  }

  .info-lead {
    position: absolute;
    font-family: "Open Sans", sans-serif; font-weight: 600;
    font-size: 42px; line-height: 1; color: var(--white);
  }
  .info-lead--1 { left: 392px; top: 792px; }
  .info-lead--2 { left: 404px; top: 836px; }
  .info-item {
    position: absolute;
    font-family: "Luckiest Guy", sans-serif;
    color: var(--gold); line-height: 1; white-space: nowrap;
  }
  .info-item--food { left: 420px; top: 890px; font-size: 56px; }
  .info-item--music { left: 444px; top: 950px; font-size: 56px; }
  .info-item--ent { left: 462px; top: 1020px; font-size: 38px; }
  .info-item--fun { left: 480px; top: 1066px; font-size: 58px; }

  .artwork { position: absolute; }
  .artwork--basket {
    left: 44px; top: 824px; width: 200px; height: 256px;
    border-radius: 14px;
    background: linear-gradient(160deg, #d9605a 0%, #a8643a 55%, #7d4a26 100%);
  }
  .artwork--monkey {
    left: 250px; top: 800px; width: 134px; height: 288px;
    border-radius: 50px;
    background: linear-gradient(180deg, #c9a06a 0%, #9c6a45 55%, #7d5236 100%);
    opacity: 0.85;
  }

  .tickets-text {
    position: absolute; left: 24px; top: 1104px;
    font-family: "Oswald", sans-serif; font-weight: 500;
    font-size: 26px; line-height: 1.2; color: var(--white); white-space: nowrap;
  }
</style>
</head>
<body>
<main class="poster">

  <svg class="layer banner" viewBox="0 0 848 1200" aria-hidden="true">
    <path d="M52 148 Q430 40 815 152 L790 282 Q430 186 82 282 Z" fill="#1a1a1a" transform="translate(4 10)"/>
    <path d="M52 148 Q430 40 815 152 L790 282 Q430 186 82 282 Z" fill="var(--red)"/>
  </svg>
  <div class="banner-title">Brook &amp; Meadow</div>

  <h1>
    <span class="event-title event-title--line1">Maple</span>
    <span class="event-title event-title--line2">Jubilee of</span>
    <span class="event-title event-title--line3">Peoples</span>
  </h1>

  <p class="event-date">October 14th 12:00-4:00pm</p>

  <svg class="layer info-panel" viewBox="0 0 848 1200" aria-hidden="true">
    <polygon points="344,760 848,760 848,1200 452,1200" fill="var(--brown)"/>
  </svg>

  <div class="artwork artwork--basket" role="img" aria-label="Vintage wooden crate brimming with red apples, with a small planet earth nestled among them"></div>
  <div class="artwork artwork--monkey" role="img" aria-label="Cartoon monkey hanging by one arm from a green vine"></div>

  <p class="info-lead info-lead--1">CELEBRATE AN</p>
  <p class="info-lead info-lead--2">AFTERNOON OF</p>
  <p class="info-item info-item--food">GREAT FOOD,</p>
  <p class="info-item info-item--music">MUSIC,</p>
  <p class="info-item info-item--ent">ENTERTAINMENT,</p>
  <p class="info-item info-item--fun">FUN</p>

  <svg class="layer tickets-bar" viewBox="0 0 848 1200" aria-hidden="true">
    <polygon points="0,1088 436,1088 446,1156 0,1156" fill="var(--ink)"/>
  </svg>
  <p class="tickets-text">Tickets will be available for sale at Pickup</p>

  <svg class="layer poster-frame" viewBox="0 0 848 1200" aria-hidden="true">
    <rect x="6" y="6" width="836" height="1188" fill="none" stroke="var(--frame)" stroke-width="3"/>
    <rect x="16" y="16" width="816" height="1168" fill="none" stroke="var(--frame)" stroke-width="1.2" opacity="0.7"/>
  </svg>
</main>
</body>
</html>
```